Updated Business Card Re-design (Logo Provided)

I am needing to update our business cards for our practice, Bright Harbor Care. We are a personal injury and wellness practice. The final design should be elegant and classy, but a type of card people would want to keep. Any samples should only have Dr. Tarek Minouvel on the template.
Updates

Went on vacation/holiday

Need extra days to review

Target Market(s)

Personal Injury clients, wellness clients

Industry/Entity Type

Personal Injury, medical, wellness

Contact Information for Business Card

dr and practice name, offerings

Requirements
Must have
• Single sided, this will be printed on a transparent business card, no exceptions.

```html
<!DOCTYPE html>
<html lang="en">
<head>
<meta charset="utf-8">
<title>Bright Harbor Care – Business Card</title>
<link href="https://fonts.googleapis.com/css2?family=Arimo:wght@400;700&family=Poppins:wght@400;700&display=swap" rel="stylesheet">
<style>
  :root{
    --card-black:#070809;
    --page:#f4f4f2;
    --orange:#f0902a;
    --gold:#b8923a;
    --green:#2e9450;
    --teal:#1f8a8a;
    --blue:#0e72c4;
    --white:#ffffff;
  }
  html,body{margin:0;padding:0;width:1200px;height:1200px;overflow:hidden;background:var(--page);}
  .card{
    position:absolute;left:50px;top:286px;width:1100px;height:628px;
    background:var(--card-black);border-radius:48px;overflow:hidden;
    font-family:"Arimo",Arial,sans-serif;color:var(--white);
  }
  .header-band{position:absolute;left:0;top:0;width:1100px;height:210px;}
  .abs{position:absolute;margin:0;white-space:nowrap;}
  .practice-name{left:79px;top:78px;font-size:49px;font-weight:700;line-height:1;}
  .practice-sub{left:79px;top:132px;font-size:38px;font-weight:400;line-height:1;}
  .doctor{left:79px;top:229px;font-size:25px;font-weight:700;color:var(--orange);line-height:1;}
  .rule{left:79px;top:309px;width:942px;height:1px;
    background:linear-gradient(90deg,#555 0%,var(--orange) 8%,var(--orange) 92%,#555 100%);}
  .brand-mark{left:760px;top:110px;width:270px;text-align:center;}
  .brand-mark .dot{display:block;margin:0 auto 12px;width:34px;height:34px;border-radius:50%;background:var(--orange);}
  .brand-mark .name{font-size:30px;font-weight:700;color:var(--blue);line-height:1.05;white-space:normal;}
  .contact-icon{position:absolute;}
  .phone{left:126px;font-size:25px;letter-spacing:2.5px;line-height:1;}
  .email{left:119px;top:405px;font-size:25px;line-height:1;}
  .web{left:119px;top:454px;font-family:"Poppins",sans-serif;font-size:22px;letter-spacing:1.5px;line-height:1;}
  .address{left:79px;top:522px;font-family:"Poppins",sans-serif;font-weight:700;font-size:23px;line-height:1;}
  .service{left:791px;font-size:25px;line-height:1;}
</style>
</head>
<body>
<div class="card">
  <svg class="header-band" viewBox="0 0 1100 210" aria-hidden="true">
    <defs>
      <linearGradient id="bandGrad" x1="0" y1="0" x2="1" y2="0.55">
        <stop offset="0" stop-color="#e8942c"/>
        <stop offset="0.4" stop-color="#2f9350"/>
        <stop offset="0.65" stop-color="#1e8a92"/>
        <stop offset="0.85" stop-color="#0c74c6"/>
      </linearGradient>
    </defs>
    <polygon points="0,0 808,0 712,195 0,195" fill="url(#bandGrad)"/>
    <polyline points="0,199 714,199 812,0" fill="none" stroke="var(--gold)" stroke-width="8"/>
    <line x1="0" y1="199" x2="400" y2="199" stroke="var(--teal)" stroke-width="8" opacity="0.7"/>
  </svg>

  <p class="abs practice-name">Bright Harbor Care</p>
  <p class="abs practice-sub">Summit Spine and Disc</p>

  <div class="abs brand-mark">
    <span class="dot"></span>
    <span class="name">Bright Harbor Care</span>
  </div>

  <p class="abs doctor">Dr. Tarek Minouvel, D.C.</p>

  <div class="abs rule"></div>

  <svg class="contact-icon" style="left:78px;top:348px" width="27" height="27" viewBox="0 0 24 24" aria-hidden="true">
    <circle cx="12" cy="12" r="12" fill="var(--green)"/>
    <path d="M8.2 6.5l2 2-1 1.4c.8 1.6 2 2.8 3.6 3.6l1.4-1 2 2-1.2 1.6c-3.8-.6-7.3-4.1-7.9-7.9z" fill="var(--card-black)"/>
  </svg>
  <p class="abs phone" style="top:335px">555.014.2286</p>
  <p class="abs phone" style="top:365px">555.019.4471</p>

  <svg class="contact-icon" style="left:78px;top:406px" width="27" height="27" viewBox="0 0 24 24" aria-hidden="true">
    <circle cx="12" cy="12" r="12" fill="var(--green)"/>
    <rect x="6" y="8" width="12" height="8" fill="none" stroke="var(--card-black)" stroke-width="1.4"/>
    <path d="M6 8l6 5 6-5M6 16l4.5-4M18 16l-4.5-4" fill="none" stroke="var(--card-black)" stroke-width="1.2"/>
  </svg>
  <p class="abs email">info@brightharborcare.com</p>

  <svg class="contact-icon" style="left:78px;top:452px" width="27" height="27" viewBox="0 0 24 24" aria-hidden="true">
    <circle cx="12" cy="12" r="12" fill="var(--green)"/>
    <g fill="none" stroke="var(--card-black)" stroke-width="1.2">
      <circle cx="12" cy="12" r="6"/><ellipse cx="12" cy="12" rx="2.6" ry="6"/>
      <line x1="6" y1="12" x2="18" y2="12"/><line x1="7" y1="9" x2="17" y2="9"/><line x1="7" y1="15" x2="17" y2="15"/>
    </g>
  </svg>
  <p class="abs web">brightharborcare.com</p>

  <svg class="contact-icon" style="left:364px;top:487px" width="24" height="31" viewBox="0 0 24 31" aria-hidden="true">
    <path d="M12 29C6 20 3 15 3 11a9 9 0 0118 0c0 4-3 9-9 18z" fill="none" stroke="var(--white)" stroke-width="2"/>
    <circle cx="12" cy="11" r="3.3" fill="none" stroke="var(--white)" stroke-width="2"/>
  </svg>
  <p class="abs address">4820 Harbor Road, Suite 12 I Lakemont, GA 30999</p>

  <svg class="contact-icon" style="left:724px;top:330px" width="44" height="24" viewBox="0 0 44 24" aria-hidden="true">
    <path d="M1 18v-6l4-5h10l4 5h2v6z" fill="var(--blue)"/>
    <path d="M23 16l1-7 5-4 9 2 4 6-1 5z" fill="var(--blue)"/>
    <circle cx="6" cy="19" r="3" fill="var(--blue)"/><circle cx="16" cy="19" r="3" fill="var(--blue)"/>
  </svg>
  <p class="abs service" style="top:330px">Auto Accident Care</p>

  <svg class="contact-icon" style="left:728px;top:369px" width="38" height="36" viewBox="0 0 38 36" aria-hidden="true">
    <path d="M4 2v8a7 7 0 0014 0V2M11 17v10a6 6 0 0012 0v-4" fill="none" stroke="var(--blue)" stroke-width="2.6"/>
    <path d="M29 20c-2-3-7-1-5 3l5 5 5-5c2-4-3-6-5-3z" fill="var(--blue)"/>
  </svg>
  <p class="abs service" style="top:375px">Primary Care</p>

  <svg class="contact-icon" style="left:732px;top:419px" width="28" height="32" viewBox="0 0 28 32" aria-hidden="true">
    <rect x="1" y="1" width="26" height="30" rx="5" fill="var(--blue)"/>
    <rect x="6" y="5" width="16" height="7" rx="2" fill="var(--card-black)"/>
  </svg>
  <p class="abs service" style="top:426px">Medical Weight loss</p>

  <svg class="contact-icon" style="left:728px;top:462px" width="40" height="32" viewBox="0 0 40 32" aria-hidden="true">
    <rect x="2" y="24" width="36" height="3" fill="var(--blue)"/>
    <rect x="2" y="29" width="36" height="2" fill="var(--blue)"/>
    <rect x="18" y="12" width="10" height="10" rx="2" fill="var(--blue)"/>
    <circle cx="24" cy="5" r="3.5" fill="var(--blue)"/>
  </svg>
  <p class="abs service" style="top:469px">Physical Therapy</p>

  <svg class="contact-icon" style="left:730px;top:510px" width="38" height="38" viewBox="0 0 38 38" aria-hidden="true">
    <rect x="2" y="22" width="34" height="4" fill="var(--blue)"/>
    <rect x="4" y="26" width="2.5" height="10" fill="var(--blue)"/>
    <rect x="31.5" y="26" width="2.5" height="10" fill="var(--blue)"/>
    <rect x="15" y="8" width="10" height="12" rx="2" fill="var(--blue)"/>
    <circle cx="21" cy="4" r="3.5" fill="var(--blue)"/>
  </svg>
  <p class="abs service" style="top:524px">Chiropractic</p>
</div>
</body>
</html>
```